OSB - Brochure 52 week Curriculum

Oakstone Brotherhood, Inc. wants to create a distribution Brochure. In the Bible (Matthew 28:18-20)- JESUS said to "TEACH" others what HE has commanded. we want to "PUT IN PRINT"

these 52 lines summarize HIS teachings
we want to use as our Curriculum teaching men ...

incorporate our statements and two main passages of scripture
(see attach pictures of headquarter lobby) to brand uniformity and consistency... we have summarized into 52 groups, but its NOT required to have numbers...
Purpose = obey GOD
Mission = love others
Vision = Development God fearing men globally.

The designer can have freedom in layout and sizing.
we were thinking bi fold , but again... designer has freedom
Please incorporate our colors (white, black, gray) using color wheel provided and our LOGO with website.

```html
<!DOCTYPE html>
<html lang="en">
<head>
<meta charset="utf-8">
<title>Jesus Said to Teach – Oakstone Brotherhood Curriculum Brochure</title>
<link href="https://fonts.googleapis.com/css2?family=Poppins:wght@400;500;600;700;800&display=swap" rel="stylesheet">
<style>
:root{
  --stage:#262626;
  --white:#ffffff;
  --ink:#111111;
  --body:#2a2a2a;
  --mid-gray:#8c8c8c;
  --heading-gray:#7a7a7a;
  --light-gray:#e6e6e8;
  --badge:#5a5a5a;
  --on-gray:#f4f4f4;
}
*{box-sizing:border-box;margin:0;padding:0}
html,body{width:1200px;height:899px;overflow:hidden;background:var(--stage)}
body{font-family:'Poppins',sans-serif;position:relative}
.spread{position:absolute;left:114px;width:972px;height:343px;background:var(--white);overflow:hidden}
.spread--outer{top:90px}
.spread--inner{top:466px}
.panel{position:absolute}
.section{position:absolute}
.section h2{font-weight:700;font-size:12.5px;line-height:1.1;margin-bottom:2.5px;color:var(--heading-gray);letter-spacing:.1px}
.section--on-gray h2{color:var(--white)}
.section--dark h2{color:var(--ink)}
.items{list-style:none;font-size:6.6px;line-height:1.15;color:var(--body)}
.section--on-gray .items{color:var(--on-gray)}
.items li{position:relative;padding-left:13px}
.items li::before{content:counter(list-item);position:absolute;left:0;top:-0.5px;width:8px;height:8px;border-radius:50%;background:var(--badge);color:var(--white);font-size:4.4px;font-weight:600;line-height:8px;text-align:center}
.section--on-gray .items li::before{background:var(--on-gray);color:var(--mid-gray)}
.gap-l li{margin-bottom:7.5px}
.gap-m li{margin-bottom:5.3px}
.gap-s li{margin-bottom:2.8px}
.title{position:absolute;left:25px;top:14px;color:#1a1a1a;font-weight:800}
.title__lead{font-size:31px;line-height:1;letter-spacing:.2px}
.title__main{font-size:67px;line-height:1;color:#000;letter-spacing:.5px;margin-top:4px}
.subtitle-band{position:absolute;left:0;top:113px}
.subtitle{position:absolute;left:27px;top:116px;color:var(--white);font-weight:700;font-size:12px;line-height:20px;letter-spacing:.2px}
.fold-shade{position:absolute;left:486px;width:60px;background:linear-gradient(90deg,rgba(0,0,0,.06),rgba(0,0,0,0))}
.ref-tag{position:absolute;left:0;top:0}
.ref-tag__text{position:absolute;left:846px;top:310px;color:var(--white);font-size:8.5px;line-height:15px;font-weight:700;letter-spacing:.4px}
.money h2{white-space:nowrap}
</style>
</head>
<body>

<section class="spread spread--outer">
  <div class="panel" style="left:486px;top:0;width:486px;height:142px;background:var(--mid-gray)"></div>
  <div class="panel" style="left:486px;top:142px;width:486px;height:201px;background:var(--light-gray)"></div>
  <div class="fold-shade" style="top:142px;height:201px"></div>

  <svg class="panel" style="left:0;top:0" width="486" height="143" role="img" aria-label="Classical painting of a haloed bearded apostle holding a book">
    <defs>
      <linearGradient id="artTop" x1="0" y1="0" x2="1" y2="1">
        <stop offset="0" stop-color="#6e6e6e"/><stop offset=".5" stop-color="#a9a9a9"/><stop offset="1" stop-color="#7d7d7d"/>
      </linearGradient>
    </defs>
    <polygon points="252,0 486,0 486,142 328,142" fill="url(#artTop)"/>
  </svg>

  <div class="title">
    <div class="title__lead">JESUS SAID TO</div>
    <div class="title__main">TEACH</div>
  </div>
  <svg class="subtitle-band" width="330" height="26"><polygon points="0,0 300,0 315,25 0,25" fill="var(--mid-gray)"/></svg>
  <div class="subtitle">OTHERS WHAT HE HAS COMMANDED</div>

  <div class="section" style="left:25px;top:176px;width:436px">
    <h2>Regarding God and Righteousness</h2>
    <ol class="items gap-l" start="1">
      <li>Repent: Change your mind and actions towards sin, as the Kingdom of Heaven is near. Turn away from sin and toward GOD. Matthew 4:17, Luke 13:3. Repent: This is the call to turn away from sin and embrace the good news of salvation through Jesus Christ. Found in Mark 1:15.</li>
      <li>Accept the Good News of salvation offered through Jesus.</li>
      <li>Believe in the Son of God, Jesus Christ: This is essential for salvation and receiving the Holy Spirit. John 6:29, John 14:11</li>
      <li>Have faith in God, and trust in Jesus as the Son of God.</li>
      <li>Be born again: John 3:7 Be born again (of water and the Spirit): Experience a spiritual transformation necessary for entrance into God's Kingdom.</li>
      <li>Give your utmost devotion and affection to God. Love God with all your heart, soul, mind, and strength: Matthew 22:37-38, Mark 12:30, Luke 10:27</li>
      <li>Honor God's Law: Understand that Jesus did not come to abolish the Law but to fulfill it and to magnify its application in the heart.</li>
    </ol>
  </div>

  <div class="section section--on-gray" style="left:511px;top:17px;width:436px">
    <h2>Regarding Relationships and Ethics</h2>
    <ol class="items gap-m" start="8">
      <li>Love your Neighbor as yourself: Matthew 22:39, Mark 12:31, Luke 10:27, Leviticus 19:18. Love one another, as I have loved you: Show sacrificial love to fellow believers.</li>
      <li>The Golden Rule: Treat others as you would want to be treated. (Matthew 7:12). This encapsulates how to treat everyone with respect, kindness, and understanding.</li>
      <li>Be reconciled to your brother: Seek peace and forgiveness when relationships are broken.</li>
      <li>Go to those who offend you: Address offenses directly and privately before involving others.</li>
      <li>Forgive offenders: Extend forgiveness to those who hurt you and forgive often. Forgive others: This is essential for receiving God's forgiveness.</li>
      <li>Love your enemies and pray for those who persecute you: Matthew 5:44, Luke 6:27-28. Extend compassion even to those who mistreat you.</li>
    </ol>
  </div>

  <div class="section section--dark" style="left:511px;top:146px;width:436px">
    <h2>Regarding Personal Conduct and Attitudes</h2>
    <ol class="items gap-m" start="14">
      <li>Be baptized: Be immersed in water as a symbol of your new life in Christ.</li>
      <li>Take, eat, and drink in remembrance of Me (Communion/Lord's Supper): Participate in the commemoration of Jesus' sacrifice.</li>
      <li>Let your light shine before others: Matthew 5:16. Followers are called to live in such a way that their good deeds bring glory to GOD. Demonstrate good works to the world.</li>
      <li>Care for the less fortunate: Help those in need, such as the hungry, thirsty, strangers, naked, sick, and imprisoned, according to Luke 14:13-14, Matthew 25:31-46.</li>
      <li>Deny yourself, Take up your cross daily and follow Jesus: This signifies a commitment to discipleship, even in the face of hardship. this teaching is found in Luke 9:23-24; Matthew 16:24-25. Prioritize following Jesus above your own desires and be willing to endure hardship for His sake.</li>
      <li>Fast: Engage in fasting, but do so for the right reasons and not for outward show.</li>
      <li>Be wise as serpents and innocent as doves: Matthew 10:16</li>
      <li>Do not worry about your life or material possessions: Trust God to provide for your needs. Trust God to provide for your needs. Matthew 6:34</li>
      <li>Lay up treasures in heaven: Focus on building a spiritual inheritance rather than accumulating earthly wealth. Matthew 6:19-21</li>
      <li>Be a servant: Seek greatness through humble service to others. Serve one another: Matthew 20:25-28</li>
    </ol>
  </div>
</section>

<section class="spread spread--inner">
  <div class="panel" style="left:0;top:107px;width:972px;height:178px;background:var(--mid-gray)"></div>
  <div class="fold-shade" style="top:0;height:107px"></div>
  <div class="fold-shade" style="top:285px;height:58px"></div>

  <svg class="panel" style="left:0;top:107px" width="972" height="178" role="img" aria-label="Classical painting of a haloed bearded apostle holding a book">
    <defs>
      <linearGradient id="artSide" x1="0" y1="0" x2="1" y2="1">
        <stop offset="0" stop-color="#9a9a9a"/><stop offset=".5" stop-color="#5e5e5e"/><stop offset="1" stop-color="#8a8a8a"/>
      </linearGradient>
    </defs>
    <polygon points="878,0 972,0 972,178 848,178" fill="var(--white)"/>
    <polygon points="884,0 972,0 972,178 858,178" fill="url(#artSide)"/>
  </svg>

  <div class="section" style="left:25px;top:13px;width:436px">
    <h2>Prayer</h2>
    <ol class="items gap-s" start="24">
      <li>Jesus provided guidance on prayer, teaching that it should be done in private and with sincerity (Matthew 6:5-8).</li>
      <li>He also linked prayer to having a forgiving heart (Mark 11:25; Matthew 18:18-20). HE encouraged praying with simple faith and persistence (Luke 11:5-13; Matthew 21:21-22).</li>
      <li>Pray: Engage in prayer consistently, with sincerity and according to Jesus' example.</li>
      <li>Prayer for our enemies : Luke 23:24, Matthew 5:44</li>
      <li>Pray for others : intercession</li>
      <li>Pray for laborers: Seek God to send workers into the harvest field of souls. Pray for kingdom laborers: Matthew 9:38, Luke 10:2</li>
    </ol>
  </div>

  <div class="section section--on-gray" style="left:25px;top:111px;width:410px">
    <h2>Regarding Outreach and Discipleship</h2>
    <ol class="items gap-l" start="30">
      <li>Go and make disciples of all nations: Evangelize and teach others to follow Jesus' commands: This is a central command, emphasizing the importance of evangelism and discipleship. Matthew 28:18-20. Teach others to obey all that Jesus commanded: Passing on the teachings of Christ to new believers is a key aspect of discipleship.</li>
      <li>Feed My Sheep: Care for and nourish the spiritual lives of believers.</li>
      <li>Receive God's power: Be filled with the Holy Spirit to effectively carry out God's work.</li>
    </ol>
  </div>

  <div class="section section--on-gray" style="left:25px;top:199px;width:436px">
    <h2>Cautions and warnings</h2>
    <ol class="items gap-l" start="33">
      <li>Beware of false prophets: Be discerning and recognize those who may mislead others with false teachings.</li>
      <li>Beware of leaven (doctrine) of the Pharisees and Sadducees: Avoid hypocrisy and legalism.</li>
      <li>Be alert and reliant on God's strength to overcome temptation.</li>
      <li>Do not cast pearls before swine: Use discretion and avoid sharing sacred things with those who may devalue or disrespect them.</li>
    </ol>
  </div>

  <div class="section" style="left:25px;top:290px;width:436px">
    <h2>Living as a Disciple</h2>
    <ol class="items gap-m" start="37">
      <li>37. Be merciful: Show compassion to others, just as God is merciful. Act with kindness and compassion towards others. Luke 6:36</li>
      <li>38. Care for those in distress: Help the hungry, thirsty, strangers, naked, sick, and imprisoned.</li>
    </ol>
  </div>

  <div class="section" style="left:511px;top:15px;width:430px">
    <ol class="items gap-l" start="39">
      <li>Recognize your own imperfections and avoid judging others harshly. Matthew 7:1-2, Luke 6:37. Focus on examining your own faults before criticizing others. He taught against judging others, stating that the standard by which you judge will be applied to you (Matthew 7:1-2).</li>
      <li>Seek God's kingdom first: Make God and his righteousness your highest priority. Prioritize God's reign and right way of living above all else. Found in Matthew 6:33.</li>
      <li>Abide in JESUS: John 15:4, John 6:35, 40, 47, John 14:27.</li>
      <li>Follow JESUS: Matthew 4:19, Luke 5:28</li>
    </ol>
  </div>

  <div class="section section--on-gray" style="left:511px;top:111px;width:330px">
    <h2>Forgiveness (Jesus Taught About The Importance Of Both Receiving And Giving Forgiveness)</h2>
    <ol class="items gap-m" start="43">
      <li>Forgive others: Matthew 6:12, 14, Mark 11:25-26, Luke 6:37</li>
      <li>JESUS emphasized that forgiveness is linked to forgiving others (Matthew 6:14-15)</li>
      <li>forgiveness should be extended limitlessly to those who repent (Luke 17:3-4; Matthew 18:21-22).</li>
      <li>forgiveness is also illustrated as the cancellation of debt (Matthew 18:21-35).</li>
    </ol>
  </div>

  <div class="section section--on-gray" style="left:511px;top:194px;width:345px">
    <h2>Humility and Service</h2>
    <ol class="items gap-s" start="47">
      <li>JESUS stated that humility leads to being honored (Luke 14:11; Matthew 23:12)</li>
      <li>True greatness is found in serving others (Matthew 20:26-28).</li>
      <li>The Bible also states that God opposes the proud but shows favor to the humble (James 4:6; 1 Peter 5:5).</li>
    </ol>
  </div>

  <div class="section section--on-gray" style="left:511px;top:249px;width:340px">
    <h2>Warning Against Self-Righteousness and Judgment</h2>
    <ol class="items" start="50">
      <li>Jesus warned against hypocrisy, particularly the hypocrisy of the Pharisees (Luke 12:1).</li>
    </ol>
  </div>

  <div class="section money" style="left:511px;top:287px;width:440px">
    <h2>Money (Jesus Taught About Using Money and Possessions Responsibly.</h2>
    <ol class="items gap-m" start="51">
      <li>JESUS advised storing up treasures in Heaven rather than on Earth (Matthew 6:19-21)</li>
      <li>JESUS stated that it is impossible to serve both God and money (Matthew 6:24).</li>
    </ol>
  </div>

  <svg class="ref-tag" width="972" height="343"><polygon points="840,309 972,309 972,325 830,325" fill="var(--mid-gray)"/></svg>
  <div class="ref-tag__text">Matthew 28:18-20</div>
</section>

</body>
</html>
```